Podcast Cover Art for Alliance Growth Circle

We need a podcast cover design for a podcast called "Alliance Growth Circle". The podcast is about partnerships in the enterprise software business. The "cover design" is kind of like an album cover and there's a great article here about how to create a stunning Podcast cover art:

https://www.wavelumen.com/blog/10-tips-create-awesome-podcast-artwork

There are also examples in that post linked above.

The Alliance Growth Circle already has some design themes/elements that I'll attach a background image for reference so you can see the typical colors, fonts, etc.

The cover art should include the words "Alliance Growth Circle" and include the names of the two artists:

Derek Halvor
Trevor Lindqvist

It should also include the Alliance Growth Circle logo somewhere. I'll attach that.

I've attached the fonts used for the logo text.

I'll also attach photos of the two artists (2 options to choose from for each). We need your guidance on whether we should include those in some stylized way, or leave them out.

Thanks for the help!

Technical Specifications:

Square Image
3000 x 3000 pixels
Resolution of 72 dpi
PNG or JPEG file types
Colorspace RGB

Colors
0054AA
0677BA
7BADD7
CADEEF
E8F1F8

Requirements
Should not have
• Avoid overused images like microphones and headsets

```html
<!DOCTYPE html>
<html lang="en">
<head>
<meta charset="utf-8">
<title>Alliance Growth Circle Podcast – Cover Art</title>
<link rel="stylesheet" href="https://fonts.googleapis.com/css2?family=Figtree:wght@600;700;800&family=Allura&display=swap">
<style>
  :root {
    --page-bg: #ffffff;
    --cover-start: #2236a4;
    --cover-mid: #1455b0;
    --cover-end: #0478c0;
    --wash: rgba(123, 173, 215, 0.28);
    --ink: #ffffff;
    --sans: "Figtree", "Helvetica Neue", Arial, sans-serif;
    --script: "Allura", "Brush Script MT", cursive;
  }

  html, body {
    margin: 0;
    padding: 0;
    width: 1200px;
    height: 1200px;
    overflow: hidden;
    background: var(--page-bg);
  }

  .canvas {
    position: relative;
    width: 1200px;
    height: 1200px;
  }

  .cover {
    position: absolute;
    left: 158px;
    top: 147px;
    width: 900px;
    height: 900px;
    overflow: hidden;
    background: linear-gradient(90deg, var(--cover-start) 0%, var(--cover-mid) 50%, var(--cover-end) 100%);
    color: var(--ink);
  }

  .cover__wash {
    position: absolute;
    inset: 0;
    background: radial-gradient(circle at 48% 55%, var(--wash) 0%, rgba(123, 173, 215, 0.12) 45%, rgba(123, 173, 215, 0) 70%);
  }

  .brand {
    position: absolute;
    left: 640px;
    top: 60px;
    width: 215px;
    text-align: center;
  }

  .brand__mark {
    display: block;
    margin: 0 auto 12px;
  }

  .brand__name {
    font-family: var(--sans);
    font-weight: 700;
    font-size: 11.5px;
    letter-spacing: 0.2px;
    text-transform: uppercase;
    white-space: nowrap;
  }

  .title {
    position: absolute;
    left: 50px;
    top: 280px;
    margin: 0;
    font-weight: normal;
  }

  .title__the {
    display: block;
    font-family: var(--script);
    font-size: 118px;
    line-height: 1;
    margin-left: 6px;
    height: 86px;
  }

  .title__line {
    display: block;
    font-family: var(--sans);
    font-weight: 700;
    font-size: 94px;
    letter-spacing: -1px;
    line-height: 112px;
    white-space: nowrap;
  }

  .title__podcast {
    font-family: var(--script);
    font-weight: normal;
    font-size: 132px;
    letter-spacing: 0;
    margin-left: 26px;
    vertical-align: -8px;
  }

  .hosts {
    position: absolute;
    left: 250px;
    width: 400px;
    top: 690px;
    text-align: center;
  }

  .hosts__with {
    display: block;
    font-family: var(--script);
    font-size: 54px;
    line-height: 50px;
  }

  .hosts__name {
    display: block;
    font-family: var(--sans);
    font-weight: 700;
    font-size: 43px;
    line-height: 52px;
    white-space: nowrap;
  }
</style>
</head>
<body>
  <main class="canvas">
    <section class="cover">
      <div class="cover__wash"></div>

      <div class="brand">
        <svg class="brand__mark" width="50" height="50" viewBox="0 0 50 50" aria-hidden="true">
          <circle cx="25" cy="25" r="22" fill="none" stroke="#ffffff" stroke-width="4"/>
        </svg>
        <div class="brand__name">Alliance Growth Circle</div>
      </div>

      <h1 class="title">
        <span class="title__the">The</span>
        <span class="title__line">Alliance Growth</span>
        <span class="title__line">Circle<span class="title__podcast">Podcast</span></span>
      </h1>

      <div class="hosts">
        <span class="hosts__with">with</span>
        <span class="hosts__name">Derek Halvor</span>
        <span class="hosts__name">&amp; Trevor Lindqvist</span>
      </div>
    </section>
  </main>
</body>
</html>
```